Eye Catching Stylish Seminar Flyer

Design a Business Seminar Flyer that will be used for Print and Web distribution that is professional, eye catching in its color scheme and fonts.

have www.bluelanternforum.example to register

Target Market(s)

Who is this for: business owners, marketplace professionals, homemakers.

Industry/Entity Type

Business Consultant

Font styles to use
Serif

Colors
abd037

Requirements
Must have
• Great colors, great Font
Nice to have
• Design a simple professional text based Logo for the Event that encapsulates For the flyer. Eye catching designs that provoke action in the reader of the flyer.
Should not have
• Cross designs stereotypical designs that are associated with religion. Rather they should be creative toward people that own businesses and work with colleagues in a daily office, school etc.

```html
<!DOCTYPE html>
<html lang="en">
<head>
<meta charset="utf-8">
<title>Blue Lantern Forum – Seminar Flyer</title>
<link href="https://fonts.googleapis.com/css2?family=Cinzel:wght@400;600;700&family=Oswald:wght@500;600&family=Open+Sans:wght@400&display=swap" rel="stylesheet">
<style>
  :root{
    --wine:#7d1a2d;
    --wine-dark:#6a1425;
    --orange:#e8672a;
    --orange-bright:#f07424;
    --ink:#1c1c1c;
    --sky-top:#eef5fb;
    --sky-mid:#c7e0f4;
    --sky-low:#a9d2f1;
    --band-light:#ffffff;
    --band-grey:#e4e4e4;
    --page:#ececec;
  }
  *{margin:0;padding:0;box-sizing:border-box}
  html,body{width:1200px;height:1200px;overflow:hidden;background:var(--page)}
  .flyer{position:absolute;left:136px;top:0;width:928px;height:1200px;overflow:hidden;background:#fff}
  .sky{position:absolute;inset:0 0 260px 0;background:linear-gradient(180deg,var(--sky-top) 0%,var(--sky-mid) 45%,var(--sky-low) 75%,#d9ebf8 100%)}
  .center{position:absolute;left:0;width:100%;text-align:center}
  .brand-mark{position:absolute;left:434px;top:42px;width:60px;height:60px;background:var(--wine)}
  .brand-name{top:120px;font-family:'Cinzel',serif;font-weight:600;color:var(--wine);font-size:40px;line-height:44px;letter-spacing:2px}
  .presents{top:258px;font-family:'Cinzel',serif;font-size:18px;letter-spacing:1.5px;color:var(--ink)}
  .title-top{top:312px;font-family:'Cinzel',serif;font-weight:700;font-size:44px;color:var(--wine);letter-spacing:1px}
  .title-main{top:360px;font-family:'Oswald',sans-serif;font-weight:600;font-size:80px;line-height:92px;color:var(--orange);letter-spacing:-1px;transform:scaleY(1.05)}
  .subtitle{top:452px;font-family:'Cinzel',serif;font-weight:600;font-size:29px;color:var(--wine);letter-spacing:1.5px}
  .rule{position:absolute;left:192px;top:516px;width:552px;height:1px;background:#6b6b6b}
  .date{position:absolute;top:528px;width:260px;text-align:center;font-family:'Cinzel',serif}
  .date.first{left:194px}
  .date.second{left:484px}
  .date .day{font-size:29px;font-weight:600;color:var(--ink);line-height:34px}
  .date .time{font-size:27px;color:var(--wine);line-height:32px}
  .date-divider{position:absolute;left:467px;top:536px;width:1px;height:54px;background:#6b6b6b}
  .fee-dome{position:absolute;left:318px;top:648px;width:300px;height:150px;border-radius:150px 150px 0 0;background:linear-gradient(180deg,#8c2236,var(--wine-dark));border:5px solid var(--orange-bright);border-bottom:none}
  .fee-label{top:680px;font-family:'Oswald',sans-serif;font-weight:500;font-size:54px;color:#fff}
  .fee-box{position:absolute;left:242px;top:749px;width:452px;height:100px;background:linear-gradient(180deg,#f47a2c,#ec6a22);border:4px solid var(--wine);border-radius:6px;box-shadow:0 8px 10px rgba(0,0,0,.18);display:flex;align-items:center;justify-content:center;text-align:center;font-family:'Cinzel',serif;font-weight:600;font-size:18.5px;line-height:24px;color:#fff;letter-spacing:1px}
  .speakers-band{position:absolute;left:0;top:940px;width:100%;height:107px;background:linear-gradient(180deg,var(--band-light),#efefef);border-top:2px solid var(--wine);border-bottom:2px solid var(--wine)}
  .speakers-tab{position:absolute;left:360px;top:926px;width:216px;height:34px;background:var(--wine);border-radius:0 0 10px 10px;color:#fff;font-family:'Cinzel',serif;font-size:19px;letter-spacing:1px;text-align:center;line-height:34px}
  .speakers{position:absolute;left:22px;top:975px;width:884px;display:flex;justify-content:space-between}
  .speaker{width:170px;text-align:center}
  .speaker .name{font-family:'Oswald',sans-serif;font-weight:500;font-size:18px;color:var(--orange);letter-spacing:.3px}
  .speaker .role{font-family:'Open Sans',sans-serif;font-size:13px;color:var(--ink);margin-top:4px}
  .tagline-band{position:absolute;left:0;top:1049px;width:100%;height:98px;background:linear-gradient(180deg,#fafafa,var(--band-grey));display:flex;align-items:center;justify-content:center;text-align:center;font-family:'Cinzel',serif;font-weight:600;font-size:18px;line-height:22px;color:var(--ink);letter-spacing:.6px;padding:0 50px}
  .footer{position:absolute;left:0;top:1147px;width:100%;height:53px;background:var(--wine);display:flex;align-items:center;justify-content:center;gap:140px;font-family:'Open Sans',sans-serif;font-size:14px;letter-spacing:1.2px;color:#fff}
  .footer span{display:flex;align-items:center;gap:9px}
  .dot{width:18px;height:18px;border-radius:50%;background:var(--orange-bright);display:inline-block}
</style>
</head>
<body>
<div class="flyer">
  <div class="sky" role="img" aria-label="Soft blue sky with light white clouds"></div>

  <div class="brand-mark"></div>
  <div class="center brand-name">BLUE LANTERN<br>FORUM</div>

  <div class="center presents">PRESENTS</div>
  <div class="center title-top">THE VOICE OF THE LORD</div>
  <div class="center title-main">IN THE MARKETPLACE</div>
  <div class="center subtitle">M<span style="font-size:23px">OVING FROM</span> I<span style="font-size:23px">NTIMACY TO</span> I<span style="font-size:23px">MPACT</span></div>

  <div class="rule"></div>
  <div class="date first"><div class="day">MARCH 24TH</div><div class="time">6PM-9:20PM</div></div>
  <div class="date-divider"></div>
  <div class="date second"><div class="day">MARCH 25TH</div><div class="time">8:30AM-2:20PM</div></div>

  <div class="fee-dome"></div>
  <div class="center fee-label">$30 FEE</div>
  <div class="fee-box">INCLUDES CONTINENTAL BREAKFAST,<br>LUNCH, AND LIGHT REFRESHMENTS<br>THROUGHOUT THE CONFERENCE.</div>

  <div class="speakers-band"></div>
  <div class="speakers-tab">OUR FEATURING</div>
  <div class="speakers">
    <div class="speaker"><div class="name">MARCUS HALE</div><div class="role">Author/Podcaster</div></div>
    <div class="speaker"><div class="name">OWEN REYES</div><div class="role">Business leader/Trainer</div></div>
    <div class="speaker"><div class="name">CLARA HALE</div><div class="role">Writer</div></div>
    <div class="speaker"><div class="name">NADIA TORRES</div><div class="role">Business Owner</div></div>
    <div class="speaker"><div class="name">PETER WALSH</div><div class="role">Business Owner</div></div>
  </div>

  <div class="tagline-band">CLARITY OF HOW GOD SPEAKS AND WHAT HE'S SAYING. INSPIRED AND EQUIPPED TO BE<br>HIS AMBASSADOR FOR THE GREAT COMMISSION.</div>

  <div class="footer">
    <span><i class="dot"></i>www.bluelanternforum.example</span>
    <span><i class="dot"></i>@lanternforum</span>
  </div>
</div>
</body>
</html>
```